Corvane Capital LLC
I need single sided standard sized Business Card [3.5" x 2"]
Fonts to be determined by designer
Professional
Derek Halloway
Chairman
Kestrel Hall Tower
418 North Larkin Avenue
Los Angeles, CA 90099
555.014.2739 X1
Acquisitions@Corvane-Capital.net
http://www.Corvane-Capital.net
We want to see what designs are out there for a cutting edge business card that shows off our 3 main goals: Intense - Expressive - Important . The business card can be vertical or horizontal, can use fonts of the designer's choice and be relatively "unique". More than just a simple black on white business card.
Use the logo and CORVANE but you do not need to use the blue background if your design does not warrant it. Financial LLC can be in any font you desire if it matches your design

```html
<!DOCTYPE html>
<html lang="en">
<head>
<meta charset="utf-8">
<title>Corvane Capital LLC — Business Card</title>
<link rel="stylesheet" href="https://fonts.googleapis.com/css2?family=Source+Sans+3:wght@400;600;700&display=swap">
<style>
  :root {
    --page-bg: #e9e6e2;
    --card-bg: #ffffff;
    --gold-dark: #a8761c;
    --gold-mid: #d4a640;
    --gold-light: #f3dc96;
    --accent-brown: #9a6a1f;
    --ink: #1b1b1b;
    --mark-fill: #1f2a2c;
  }
  * { box-sizing: border-box; margin: 0; padding: 0; }
  html, body {
    width: 1200px;
    height: 965px;
    overflow: hidden;
    background: var(--page-bg);
    font-family: "Source Sans 3", "Myriad Pro", Arial, sans-serif;
  }
  .business-card {
    position: absolute;
    left: 215px;
    top: 262px;
    width: 770px;
    height: 440px;
    background: var(--card-bg);
    border-radius: 26px;
    overflow: hidden;
    box-shadow: 0 6px 22px rgba(0,0,0,0.18);
  }
  .card-decor {
    position: absolute;
    inset: 0;
    width: 100%;
    height: 100%;
  }
  .brand-block {
    position: absolute;
    left: 20px;
    top: 70px;
    width: 320px;
    text-align: center;
  }
  .brand-square {
    display: block;
    width: 96px;
    height: 96px;
    margin: 0 auto 22px;
    background: var(--mark-fill);
  }
  .brand-name {
    font-size: 40px;
    font-weight: 600;
    letter-spacing: 3px;
    line-height: 1.1;
    color: var(--accent-brown);
    text-transform: uppercase;
  }
  .divider {
    position: absolute;
    left: 362px;
    top: 42px;
    width: 2px;
    height: 360px;
    background: linear-gradient(to bottom, var(--gold-light), var(--gold-dark), var(--gold-light));
  }
  .contact-block {
    position: absolute;
    left: 380px;
    top: 58px;
    width: 380px;
    color: var(--ink);
  }
  .person-name {
    font-size: 27px;
    font-weight: 700;
    color: var(--accent-brown);
    line-height: 1.1;
  }
  .person-title {
    font-size: 21px;
    font-weight: 400;
    margin-top: 2px;
    margin-bottom: 22px;
  }
  .contact-line {
    font-size: 19px;
    line-height: 31px;
    white-space: nowrap;
  }
  .contact-label {
    font-weight: 700;
    color: var(--accent-brown);
  }
</style>
</head>
<body>
  <div class="business-card">
    <svg class="card-decor" viewBox="0 0 770 440" aria-hidden="true">
      <defs>
        <linearGradient id="goldSweep" x1="0" y1="0" x2="1" y2="1">
          <stop offset="0" stop-color="#f3dc96"/>
          <stop offset="0.45" stop-color="#d4a640"/>
          <stop offset="1" stop-color="#9c6b17"/>
        </linearGradient>
      </defs>
      <!-- top-right band -->
      <path d="M520 0 C640 12 735 70 770 185 L770 0 Z" fill="url(#goldSweep)"/>
      <path d="M505 0 C635 16 738 82 770 200" fill="none" stroke="#111" stroke-width="5"/>
      <!-- bottom-left band -->
      <path d="M0 240 C30 330 95 410 190 440 L0 440 Z" fill="url(#goldSweep)"/>
      <path d="M0 226 C35 325 100 405 205 440" fill="none" stroke="#111" stroke-width="5"/>
    </svg>

    <div class="brand-block">
      <span class="brand-square"></span>
      <div class="brand-name">Corvane Capital LLC</div>
    </div>

    <div class="divider"></div>

    <div class="contact-block">
      <div class="person-name">Derek Halloway</div>
      <div class="person-title">Chairman</div>
      <div class="contact-line">Kestrel Hall Tower</div>
      <div class="contact-line">418 North Larkin Avenue</div>
      <div class="contact-line">Los Angeles, CA 90099</div>
      <div class="contact-line"><span class="contact-label">Phone</span> : 555.014.2739 X1</div>
      <div class="contact-line"><span class="contact-label">Fax</span> : 555.014.2740</div>
      <div class="contact-line"><span class="contact-label">Email</span> : Acquisitions@Corvane-Capital.net</div>
      <div class="contact-line"><span class="contact-label">Web</span> : http://www.Corvane-Capital.net</div>
    </div>
  </div>
</body>
</html>
```